Web App Design Project

Need to provide graphical design of 2 web pages according to attached wireframes.

Colors should be adjusted for the 65+ population meaning not too bright.

App logo should be created as well - logo should represent long and good life.

Target Market(s)

65 years old and above

```html
<!DOCTYPE html>
<html lang="en">
<head>
<meta charset="utf-8">
<title>Vitalong – Medications</title>
<link rel="stylesheet" href="https://fonts.googleapis.com/css2?family=Arimo:wght@400;700&display=swap">
<style>
:root{
  --page-bg:#e9eaeb;
  --header-top:#63c7f5;
  --header-bottom:#3b98d6;
  --header-line:#2f86c4;
  --btn-top:#4fb3ea;
  --btn-bottom:#2f8ccc;
  --panel-grey:#f3f3f4;
  --divider:#e0e0e3;
  --white:#ffffff;
  --text:#6c6f7e;
  --text-soft:#8d909c;
  --text-strong:#4f5260;
  --accent-blue:#3b98d6;
  --green:#5cb85c;
  --green-border:#6cc06c;
  --grey-btn:#8f929e;
  --card-border:#c9cad6;
  --nav-bg:#373a48;
  --nav-active:#5c5f6d;
  --nav-divider:#2e3140;
  --nav-text:#c9cbd3;
  --nav-icon:#c3c5cd;
}
*{box-sizing:border-box;margin:0;padding:0}
html,body{width:1200px;height:900px;overflow:hidden}
body{
  background:radial-gradient(ellipse at center,#f6f6f7 0%,var(--page-bg) 75%);
  font-family:"Arimo",Arial,sans-serif;color:var(--text);position:relative;
}
.app{position:absolute;left:100px;top:120px;width:1000px;height:660px;background:var(--white);
  box-shadow:0 12px 40px rgba(0,0,0,.22)}
/* header */
.topbar{position:absolute;left:0;top:0;width:1000px;height:60px;
  background:linear-gradient(var(--header-top),var(--header-bottom));border-bottom:1px solid var(--header-line)}
.brand{position:absolute;left:0;top:0;width:200px;height:60px;border-right:1px solid rgba(255,255,255,.25)}
.brand-mark{position:absolute;left:22px;top:13px;width:34px;height:34px;border-radius:50%;background:#e8f6fd}
.brand-name{position:absolute;left:73px;top:13px;color:var(--white);font-weight:700;font-size:19px}
.brand-slogan{position:absolute;left:73px;top:34px;color:var(--white);font-weight:700;font-size:9px}
.welcome{position:absolute;left:215px;top:21px;color:#e6f4fc;font-size:16px}
.welcome strong{color:var(--white)}
.text-size{position:absolute;top:0;color:var(--white);line-height:60px}
.search{position:absolute;left:686px;top:14px;width:163px;height:31px;border:1px solid rgba(255,255,255,.5);
  background:rgba(255,255,255,.12);color:#dff1fb;font-size:14px;padding:8px 9px}
.search svg{position:absolute;right:8px;top:7px}
.top-btn{position:absolute;top:14px;height:31px;border:1px solid #2a7fbd;
  background:linear-gradient(var(--btn-top),var(--btn-bottom));color:var(--white);font-weight:700;
  font-size:16px;text-align:center;line-height:29px}
/* sub header */
.subbar{position:absolute;left:0;top:61px;width:1000px;height:69px;background:var(--panel-grey);border-bottom:1px solid var(--divider)}
.section-title{position:absolute;left:0;top:0;width:200px;line-height:69px;text-align:center;color:var(--accent-blue);
  font-size:17px;font-weight:700;border-right:1px solid var(--divider);height:69px}
.add-med{position:absolute;left:230px;top:22px;font-size:16px;font-weight:700;color:var(--text-soft);display:flex;align-items:center;gap:7px}
.settings{position:absolute;left:944px;top:22px}
/* sidebar */
.sidebar{position:absolute;left:0;top:130px;width:200px;height:400px;background:var(--panel-grey);border-right:1px solid var(--divider)}
.time-tab{position:absolute;left:0;width:200px;height:90px;display:flex;align-items:center;gap:10px;padding-left:40px;
  font-size:16px;font-weight:700;color:var(--text-soft)}
.time-tab.is-active{left:10px;width:191px;background:var(--white);color:var(--text-strong);padding-left:30px;
  box-shadow:0 2px 3px rgba(0,0,0,.06)}
/* medication list */
.med-card{position:absolute;left:230px;width:741px;height:61px;border:1px solid var(--card-border);border-radius:3px;background:var(--white)}
.med-card.is-taken{border-color:var(--green-border)}
.status-btn{position:absolute;left:14px;top:15px;width:100px;height:30px;border-radius:2px;color:var(--white);
  font-size:13px;font-weight:700;text-align:center;line-height:30px;background:var(--grey-btn)}
.status-btn.taken{background:var(--green);display:flex;align-items:center;justify-content:center;gap:7px}
.med-name{position:absolute;left:147px;top:21px;font-size:16px;color:var(--text)}
.dose{position:absolute;left:576px;top:21px;font-size:16px;font-weight:700;color:var(--text-strong)}
.dose-icon{position:absolute;left:609px;top:18px}
.info{position:absolute;left:699px;top:20px}
/* bottom nav */
.main-nav{position:absolute;left:0;top:530px;width:1000px;height:130px;background:var(--nav-bg);display:flex}
.nav-item{flex:1;border-right:1px solid var(--nav-divider);display:flex;flex-direction:column;align-items:center;
  justify-content:flex-start;padding-top:28px;color:var(--nav-text);font-size:14px;font-weight:700;text-align:center;line-height:17px}
.nav-item:last-child{border-right:0}
.nav-item svg{height:36px;margin-bottom:13px}
.nav-item .label{height:34px;display:flex;align-items:center}
.nav-item.is-active{background:var(--nav-active);color:var(--white)}
</style>
</head>
<body>
<main class="app">
  <header class="topbar">
    <div class="brand">
      <span class="brand-mark"></span>
      <span class="brand-name">Vitalong</span>
      <span class="brand-slogan">Here is your slogan</span>
    </div>
    <p class="welcome">Welcome back, <strong>Arthur Pembley</strong></p>
    <span class="text-size" style="left:611px;font-size:11px">A</span>
    <span class="text-size" style="left:632px;font-size:17px;font-weight:700">A</span>
    <span class="text-size" style="left:656px;font-size:20px">A</span>
    <div class="search">Search
      <svg width="16" height="16" viewBox="0 0 16 16" fill="none" stroke="#fff" stroke-width="2"><circle cx="6.5" cy="6.5" r="4.8"/><path d="M10 10l4.5 4.5"/></svg>
    </div>
    <span class="top-btn" style="left:888px;width:32px">?</span>
    <span class="top-btn" style="left:934px;width:52px">Exit</span>
  </header>

  <div class="subbar">
    <h1 class="section-title">Medications</h1>
    <div class="add-med">
      <svg width="26" height="26" viewBox="0 0 26 26" fill="none" stroke="#8d909c" stroke-width="2"><circle cx="13" cy="13" r="11.5"/><path d="M13 7v12M7 13h12" stroke-width="2.6"/></svg>
      Add medication
    </div>
    <svg class="settings" width="26" height="26" viewBox="0 0 26 26" fill="none" stroke="#8d909c" stroke-width="2"><circle cx="13" cy="13" r="11.5"/><circle cx="13" cy="13" r="4"/><path d="M13 5v3M13 18v3M5 13h3M18 13h3M7.3 7.3l2.1 2.1M16.6 16.6l2.1 2.1M7.3 18.7l2.1-2.1M16.6 9.4l2.1-2.1" stroke-width="3"/></svg>
  </div>

  <nav class="sidebar">
    <div class="time-tab is-active" style="top:0">
      <svg width="32" height="32" viewBox="0 0 32 32" fill="none" stroke="#6c6f7e" stroke-width="1.8"><path d="M9 16a7 7 0 0 1 14 0M16 3v4M6 7l3 3M26 7l-3 3M2 16h3M27 16h3M2 20h28M2 24h28M2 28h28"/></svg>
      Morning
    </div>
    <div class="time-tab" style="top:100px">
      <svg width="32" height="32" viewBox="0 0 32 32" fill="none" stroke="#8d909c" stroke-width="1.8"><circle cx="16" cy="16" r="7"/><path d="M16 2v4M16 26v4M2 16h4M26 16h4M6 6l3 3M23 23l3 3M6 26l3-3M23 9l3-3"/></svg>
      Noon
    </div>
    <div class="time-tab" style="top:200px">
      <svg width="34" height="34" viewBox="0 0 34 34" fill="none" stroke="#8d909c" stroke-width="1.8"><path d="M10 14a6 6 0 0 1 12-1M16 3v3M6 7l2 2M26 7l-2 2M3 14h3"/><path d="M8 30a5 5 0 0 1 0-10 7 7 0 0 1 13-2 5.5 5.5 0 0 1 6 6 3 3 0 0 1 0 6z"/></svg>
      Afternoon
    </div>
    <div class="time-tab" style="top:300px">
      <svg width="32" height="32" viewBox="0 0 32 32" fill="none" stroke="#8d909c" stroke-width="1.8"><path d="M20 3a13 13 0 1 0 10 19A12 12 0 0 1 20 3z"/></svg>
      Night
    </div>
  </nav>

  <section class="med-list">
    <article class="med-card is-taken" style="top:160px">
      <span class="status-btn taken"><svg width="11" height="9" viewBox="0 0 11 9" fill="none" stroke="#fff" stroke-width="2.2"><path d="M1 4.5l3 3L10 1"/></svg>Taken</span>
      <span class="med-name">Dolvaren (indomethacin)</span>
      <span class="dose">4x</span>
      <svg class="dose-icon" width="24" height="24" viewBox="0 0 24 24" fill="none" stroke="#6c6f7e" stroke-width="1.6"><rect x="2" y="8" width="20" height="8" rx="4" transform="rotate(-45 12 12)"/><path d="M9.2 9.2l5.6 5.6"/><path d="M4 15l5 5" stroke-width="0"/></svg>
      <svg class="info" width="20" height="20" viewBox="0 0 20 20" fill="none" stroke="#a6a8b3" stroke-width="1.2"><circle cx="10" cy="10" r="9"/><path d="M10 8.5v6M10 5.5v1.3" stroke-width="1.6"/></svg>
    </article>
    <article class="med-card" style="top:252px">
      <span class="status-btn">Mark as taken</span>
      <span class="med-name">Trombexa (dabigatran)</span>
      <span class="dose">2x</span>
      <svg class="dose-icon" width="24" height="24" viewBox="0 0 24 24" fill="none" stroke="#6c6f7e" stroke-width="1.6"><rect x="3" y="7" width="11" height="14" rx="2"/><path d="M4 4h9v3H4zM5 12h7M5 16h7"/><path d="M19 3v8M19 11v10" stroke-width="2"/><ellipse cx="19" cy="6" rx="2" ry="3"/></svg>
      <svg class="info" width="20" height="20" viewBox="0 0 20 20" fill="none" stroke="#a6a8b3" stroke-width="1.2"><circle cx="10" cy="10" r="9"/><path d="M10 8.5v6M10 5.5v1.3" stroke-width="1.6"/></svg>
    </article>
    <article class="med-card" style="top:344px">
      <span class="status-btn">Mark as taken</span>
      <span class="med-name">Gastrolin (omeprazole)</span>
      <span class="dose">1x</span>
      <svg class="dose-icon" width="24" height="24" viewBox="0 0 24 24" fill="none" stroke="#6c6f7e" stroke-width="1.6"><path d="M14 4l6 6M17 7l4-4M15 5L6 14l4 4 9-9M6 14l-3 3 4 4 3-3M9 11l2 2M11 9l2 2"/></svg>
      <svg class="info" width="20" height="20" viewBox="0 0 20 20" fill="none" stroke="#a6a8b3" stroke-width="1.2"><circle cx="10" cy="10" r="9"/><path d="M10 8.5v6M10 5.5v1.3" stroke-width="1.6"/></svg>
    </article>
  </section>

  <nav class="main-nav">
    <div class="nav-item is-active">
      <svg width="32" height="36" viewBox="0 0 32 36" fill="#fff"><rect x="3" y="2" width="9" height="22" rx="4.5" transform="rotate(-20 7 13)"/><rect x="15" y="10" width="10" height="22" rx="5" transform="rotate(-40 20 21)" fill="#fff" stroke="#5c5f6d" stroke-width="1.5"/></svg>
      <span class="label">Medications</span>
    </div>
    <div class="nav-item">
      <svg width="32" height="36" viewBox="0 0 32 36" fill="none" stroke="#c3c5cd" stroke-width="1.8"><path d="M24 3a3 3 0 0 1 4 4L13 24l-4-4z"/><path d="M9 20l-4 4a3 3 0 0 0 4 4l4-4M16 11l2 2M19 8l2 2"/></svg>
      <span class="label">Home<br>Measurements</span>
    </div>
    <div class="nav-item">
      <svg width="32" height="36" viewBox="0 0 32 36" fill="none" stroke="#c3c5cd" stroke-width="2"><rect x="2" y="6" width="28" height="26" rx="1"/><path d="M2 12h28M9 3v6M23 3v6"/><text x="16" y="28" font-size="12" fill="#c3c5cd" stroke="none" text-anchor="middle" font-family="Arimo,sans-serif">17</text></svg>
      <span class="label">My Schedule</span>
    </div>
    <div class="nav-item">
      <svg width="34" height="36" viewBox="0 0 34 36" fill="none" stroke="#c3c5cd" stroke-width="2"><rect x="2" y="3" width="30" height="22"/><path d="M6 15h6l3-6 4 11 3-5h6M11 25l-4 8M23 25l4 8M17 25v5"/></svg>
      <span class="label">Lab Test Results</span>
    </div>
    <div class="nav-item">
      <svg width="34" height="36" viewBox="0 0 34 36" fill="none" stroke="#c3c5cd" stroke-width="2"><rect x="2" y="3" width="6" height="6"/><rect x="2" y="15" width="6" height="6"/><rect x="2" y="27" width="6" height="6"/><path d="M12 6h20M12 18h20M12 30h20" stroke-width="3.4"/></svg>
      <span class="label">Checkups &amp;<br>Procedures</span>
    </div>
    <div class="nav-item">
      <svg width="32" height="36" viewBox="0 0 32 36" fill="#c3c5cd"><path d="M16 2c-5 0-7 4-6.5 9 .4 3.5 2.5 7 6.5 7s6.1-3.5 6.5-7C23 6 21 2 16 2zM3 34c0-7 5-11 9-12l4 3 4-3c4 1 9 5 9 12z"/></svg>
      <span class="label">My Profile</span>
    </div>
    <div class="nav-item">
      <svg width="34" height="36" viewBox="0 0 34 36" fill="#c3c5cd"><path d="M17 31C6 22 1 17 1 10a8 8 0 0 1 16-1 8 8 0 0 1 16 1c0 7-5 12-16 21z"/></svg>
      <span class="label">My Health Care<br>Providers</span>
    </div>
  </nav>
</main>
</body>
</html>
```